Charity fundraising company - need eDM design!

We are a telemarketing company working with charities to raise money from individuals via regular monthly direct debits or credit card payments. The audience for this eDM is a few hundred fundraising managers. We want to provide a clearly laid-out email to deliver our offer of a free telemarketing consultation.

The eDM will be sent via Mailchimp.

Industry/Entity Type

Charity

Logo Text

KELP Dial

Font styles to use
Sans Serif
Other font styles liked:
• Helvetica Neue

Requirements
Nice to have
• Our values:
• Storytelling with passion
• Fundraising with integrity
• Results that deliver a strong return on your charity's investment.
Should not have
• Logo at the top of the eDM (please place at the bottom)

```html
<!DOCTYPE html>
<html lang="en">
<head>
<meta charset="utf-8">
<title>KELP Dial – Free Consultation eDM</title>
<link rel="stylesheet" href="https://fonts.googleapis.com/css2?family=Open+Sans:wght@400;600;700&display=swap">
<style>
  :root {
    --page-bg: #3a3a3a;
    --header-bg: #f8f8f8;
    --white: #ffffff;
    --green: #9ccb5a;
    --purple: #5e5a8a;
    --purple-dark: #4a4468;
    --grey-band: #ebebeb;
    --text-grey: #666666;
    --text-light: #8a8a8a;
    --icon-blue: #29a8e0;
    --brand-red: #a3141c;
  }
  * { box-sizing: border-box; margin: 0; padding: 0; }
  html, body { width: 960px; height: 1200px; overflow: hidden; }
  body {
    background: var(--page-bg);
    font-family: "Open Sans", "Helvetica Neue", Arial, sans-serif;
  }
  .edm {
    position: absolute; left: 30px; top: 51px;
    width: 900px; height: 1098px;
    background: var(--white);
    display: flex; flex-direction: column;
  }
  .edm-header {
    height: 72px; background: var(--header-bg);
    display: flex; align-items: center; justify-content: flex-end;
    padding: 0 52px 0 42px;
  }
  .main-nav { display: flex; gap: 25px; }
  .main-nav a { font-size: 18px; color: var(--text-grey); text-decoration: none; }

  .headline-band {
    height: 69px; background: var(--green);
    display: flex; align-items: center; justify-content: center;
  }
  .headline-band h1 { font-size: 26px; font-weight: 600; color: var(--white); }

  .intro-row, .offer-row { display: flex; }
  .intro-row { height: 276px; }
  .intro-copy {
    width: 450px; background: var(--purple);
    display: flex; align-items: center; justify-content: center;
    padding: 0 48px; text-align: center;
  }
  .intro-copy p { font-size: 22px; font-weight: 700; line-height: 1.3; color: var(--white); }
  .photo-agent {
    width: 450px;
    background: linear-gradient(135deg, #1e1e1e 0%, #3a332e 45%, #7a6352 70%, #1a1a1a 100%);
  }

  .offer-row { height: 450px; }
  .photo-headset {
    width: 450px;
    background: radial-gradient(ellipse at 55% 45%, #f2f2f2 0%, #cfcfcf 55%, #9a9a9a 100%);
  }
  .offer { width: 450px; padding: 14px 8px 0 17px; }
  .offer h2 {
    font-size: 22px; font-weight: 600; color: var(--text-grey);
    text-align: center; margin-bottom: 18px;
  }
  .offer-list { list-style: none; }
  .offer-list li {
    display: flex; gap: 15px; align-items: flex-start;
    font-size: 16px; line-height: 1.4; color: var(--text-light);
    margin-bottom: 14px;
  }
  .offer-list svg { flex: 0 0 22px; margin-top: 2px; }
  .cta {
    margin-top: 12px; width: 415px; height: 77px;
    background: var(--purple-dark); border-radius: 39px;
    display: flex; flex-direction: column; align-items: center; justify-content: center;
    color: var(--white); text-decoration: none; text-align: center;
  }
  .cta-title { font-size: 17px; font-weight: 700; letter-spacing: 0.3px; }
  .cta-sub { font-size: 16px; font-weight: 600; margin-top: 4px; }

  .contact-band {
    height: 122px; background: var(--grey-band);
    display: flex; align-items: center; padding: 0 18px;
  }
  .contact-address { width: 532px; display: flex; align-items: center; gap: 20px; }
  .contact-address p, .contact-item span { font-size: 17px; line-height: 1.45; color: var(--text-light); }
  .contact-details { display: flex; flex-direction: column; gap: 12px; }
  .contact-item { display: flex; align-items: center; gap: 16px; }

  .brand-row {
    height: 57px; background: var(--header-bg);
    display: flex; align-items: center; justify-content: center; gap: 10px;
  }
  .brand-mark { width: 16px; height: 16px; background: var(--brand-red); }
  .brand-name { font-size: 24px; font-weight: 700; color: var(--brand-red); }

  .edm-footer {
    height: 52px; background: var(--purple);
    display: flex; align-items: center; justify-content: space-between;
    padding: 0 38px 0 35px;
  }
  .edm-footer p, .edm-footer a { font-size: 16px; color: var(--white); text-decoration: none; }
</style>
</head>
<body>
  <main class="edm">
    <header class="edm-header">
      <nav class="main-nav">
        <a href="#">Home</a>
        <a href="#">About Us</a>
        <a href="#">Contact</a>
      </nav>
    </header>

    <section class="headline-band">
      <h1>Want more regular givers for your cause?</h1>
    </section>

    <section class="intro-row">
      <div class="intro-copy">
        <p>KELP Dial is Australia’s leading telemarketing specialist for acquiring new regular givers through lead generation.</p>
      </div>
      <div class="photo-agent" role="img" aria-label="Photo of a smiling call centre agent wearing a headset at a computer"></div>
    </section>

    <section class="offer-row">
      <div class="photo-headset" role="img" aria-label="Photo of a black headset resting on a white surface"></div>
      <div class="offer">
        <h2>Speak to us today and we will:</h2>
        <ul class="offer-list">
          <li>
            <svg width="22" height="22" viewBox="0 0 26 26" aria-hidden="true"><path d="M20 6.5A10 10 0 1 0 23 13" fill="none" stroke="#8a8a8a" stroke-width="3" stroke-linecap="round"/><path d="M8 12.5l4.5 4.5L23 5" fill="none" stroke="#8a8a8a" stroke-width="3.2" stroke-linecap="round" stroke-linejoin="round"/></svg>
            <span>Run a no-obligation TM donor acquisition feasibility assessment for you.</span>
          </li>
          <li>
            <svg width="22" height="22" viewBox="0 0 26 26" aria-hidden="true"><path d="M20 6.5A10 10 0 1 0 23 13" fill="none" stroke="#8a8a8a" stroke-width="3" stroke-linecap="round"/><path d="M8 12.5l4.5 4.5L23 5" fill="none" stroke="#8a8a8a" stroke-width="3.2" stroke-linecap="round" stroke-linejoin="round"/></svg>
            <span>Offer a Cost Per Acquisition model, with a sliding scale of fees based on the volume of leads provided.</span>
          </li>
          <li>
            <svg width="22" height="22" viewBox="0 0 26 26" aria-hidden="true"><path d="M20 6.5A10 10 0 1 0 23 13" fill="none" stroke="#8a8a8a" stroke-width="3" stroke-linecap="round"/><path d="M8 12.5l4.5 4.5L23 5" fill="none" stroke="#8a8a8a" stroke-width="3.2" stroke-linecap="round" stroke-linejoin="round"/></svg>
            <span>Handle the entire data ordering and management process for you at no additional cost.</span>
          </li>
        </ul>
        <a class="cta" href="#">
          <span class="cta-title">FREE NO-OBLIGATION CONSULTATION</span>
          <span class="cta-sub">Drop us a line today...</span>
        </a>
      </div>
    </section>

    <section class="contact-band">
      <div class="contact-address">
        <svg width="32" height="32" viewBox="0 0 38 38" aria-hidden="true"><circle cx="19" cy="19" r="17" fill="none" stroke="#29a8e0" stroke-width="2.5"/><path d="M19 10a6 6 0 0 0-6 6c0 4.5 6 12 6 12s6-7.5 6-12a6 6 0 0 0-6-6z" fill="#29a8e0"/><circle cx="19" cy="16" r="2.3" fill="#ebebeb"/></svg>
        <p>Suite 3.04, Level 3, 18 Harbour Lane,<br>Sydney, NSW, 2000</p>
      </div>
      <div class="contact-details">
        <div class="contact-item">
          <svg width="32" height="32" viewBox="0 0 38 38" aria-hidden="true"><circle cx="19" cy="19" r="17" fill="none" stroke="#29a8e0" stroke-width="2.5"/><path d="M13 11.5l3-1 2.5 4.5-2 1.8c.9 2.2 2.5 3.8 4.7 4.7l1.8-2 4.5 2.5-1 3c-6.5.8-14.3-7-13.5-13.5z" fill="#29a8e0"/></svg>
          <span>02 5550 1234</span>
        </div>
        <div class="contact-item">
          <svg width="32" height="32" viewBox="0 0 38 38" aria-hidden="true"><circle cx="19" cy="19" r="17" fill="none" stroke="#29a8e0" stroke-width="2.5"/><g fill="none" stroke="#29a8e0" stroke-width="2.6" stroke-linecap="round"><path d="M17.5 21.5l-2.5 2.5a3 3 0 0 1-4.2-4.2l3.5-3.5a3 3 0 0 1 4.2 0"/><path d="M20.5 16.5l2.5-2.5a3 3 0 0 1 4.2 4.2l-3.5 3.5a3 3 0 0 1-4.2 0"/></g></svg>
          <span>www.kelpdial.com</span>
        </div>
      </div>
    </section>

    <section class="brand-row">
      <span class="brand-mark"></span>
      <span class="brand-name">KELP Dial</span>
    </section>

    <footer class="edm-footer">
      <p>KELP Dial 2016 All rights reserved.</p>
      <a href="#">Unsubscribe here</a>
    </footer>
  </main>
</body>
</html>
```